Flyer-Design für Initiative für bunte Freizeitkultur
Zielgruppe
Initiative für bunte Freizeitkultur. Wir haben im Januar diesen Jahres einen neuen Jugendtreff eröffnet und benötigen dafür einen Flyer der möglichst ansprechend für Jugendliche zwischen 10 und 18 Jahren ist. Der Flyer sollte beidseitig sein und die beschriebenen Vorgaben enthalten.
Aufgabenstellung
Größe A5.
Folgende Informationen müssen enthalten sein:
Vorderseite:
Name des Jugendtreffs: Jugendtreff Korvane
Träger: Initiative für bunte Freizeitkultur e.V.
Angebote: GX7 / Billard / Tischtennis / Free-Wlan / Fitness / Essen und Getränke / Werkstatt / Chillen / Räume selbst gestalten
'follow us on Fotello' inklusive fotello Logo.

```html
<!DOCTYPE html>
<html lang="de">
<head>
<meta charset="utf-8">
<title>Jugendtreff Korvane – Flyer</title>
<link rel="stylesheet" href="https://fonts.googleapis.com/css2?family=Permanent+Marker&family=Roboto:wght@400&family=Didact+Gothic&display=swap">
<style>
  :root {
    --paper: #ffffff;
    --marble-red: #c8261a;
    --marble-orange: #f0831c;
    --marble-yellow: #e9c23a;
    --marble-blue: #3aa6dc;
    --marble-sky: #8fd3f0;
    --silhouette: #050505;
    --tag-yellow: #f2ea2a;
    --tag-white: #ffffff;
    --tag-outline: #000000;
    --circle-orange: #f29100;
    --brand-red: #a8120f;
  }
  * { margin: 0; padding: 0; box-sizing: border-box; }
  html, body { width: 1200px; height: 836px; overflow: hidden; background: var(--paper); }
  .canvas { position: relative; width: 1200px; height: 836px; background: var(--paper); }

  .page { position: absolute; top: 0; height: 836px; overflow: hidden; }
  .page--front { left: 0; width: 596px; }
  .page--back { left: 605px; width: 595px; }

  .marble { position: absolute; inset: 0; }
  .page--front .marble {
    background:
      radial-gradient(ellipse 45% 30% at 20% 15%, var(--marble-yellow), transparent 70%),
      radial-gradient(ellipse 40% 35% at 80% 70%, var(--marble-sky), transparent 70%),
      radial-gradient(ellipse 50% 30% at 30% 55%, var(--marble-blue), transparent 70%),
      radial-gradient(ellipse 50% 35% at 20% 85%, var(--marble-orange), transparent 70%),
      linear-gradient(160deg, var(--marble-red), var(--marble-orange) 40%, var(--marble-red) 75%, var(--marble-orange));
  }
  .page--back .marble {
    background:
      radial-gradient(ellipse 40% 30% at 25% 12%, var(--marble-red), transparent 70%),
      radial-gradient(ellipse 35% 45% at 20% 50%, var(--marble-sky), transparent 70%),
      radial-gradient(ellipse 45% 30% at 60% 35%, var(--marble-blue), transparent 70%),
      radial-gradient(ellipse 40% 30% at 45% 75%, var(--marble-red), transparent 70%),
      linear-gradient(200deg, var(--marble-orange), var(--marble-red) 45%, var(--marble-orange) 80%, var(--marble-red));
  }

  .silhouette { position: absolute; background: var(--silhouette); border-radius: 40px 40px 6px 6px; }
  .silhouette--front { left: 358px; top: 397px; width: 133px; height: 423px; }
  .silhouette--back { left: 409px; top: 0; width: 133px; height: 303px; border-radius: 6px 6px 40px 40px; }

  .brand-mark {
    position: absolute; left: 337px; top: 10px; width: 174px; height: 174px; border-radius: 50%;
    background: var(--circle-orange);
    display: flex; align-items: center; justify-content: center;
  }
  .brand-name {
    width: 140px; text-align: center;
    font-family: "Roboto", sans-serif; font-size: 19px; line-height: 1.2; color: var(--brand-red);
  }
  .treff-name { position: absolute; right: 46px; top: 183px; font-family: "Roboto", sans-serif; font-size: 24px; line-height: 1.2; color: var(--tag-white); white-space: nowrap; }
  .treff-carrier { position: absolute; right: 43px; top: 214px; font-family: "Roboto", sans-serif; font-size: 14px; line-height: 1.2; color: var(--tag-white); white-space: nowrap; }

  .tag {
    position: absolute; font-family: "Permanent Marker", cursive; color: var(--tag-white);
    text-transform: uppercase; line-height: 1; white-space: nowrap; font-size: 30px;
    text-shadow: 2px 0 var(--tag-outline), -2px 0 var(--tag-outline), 0 2px var(--tag-outline), 0 -2px var(--tag-outline), 2px 2px var(--tag-outline), -2px -2px var(--tag-outline), 2px -2px var(--tag-outline), -2px 2px var(--tag-outline);
  }
  .tag--up { transform-origin: left top; transform: rotate(-90deg); }
  .tag--down { transform-origin: left top; transform: rotate(90deg); }
  .tag--title { color: var(--tag-yellow); font-size: 44px; letter-spacing: 3px; }

  .handle-block {
    position: absolute; left: 62px; top: 204px; width: 365px; height: 54px;
    transform: rotate(180deg);
    display: flex; align-items: center; justify-content: flex-end; gap: 13px;
  }
  .handle-text { text-align: right; }
  .handle-icon { width: 50px; height: 50px; border-radius: 10px; background: var(--circle-orange); flex: none; }
  .handle-follow { font-family: "Roboto", sans-serif; font-size: 15px; line-height: 1.2; color: var(--tag-white); }
  .handle-name {
    font-family: "Permanent Marker", cursive; text-transform: uppercase; font-size: 23px; line-height: 1.1; color: var(--tag-yellow);
    text-shadow: 1px 1px var(--tag-outline), -1px -1px var(--tag-outline), 1px -1px var(--tag-outline), -1px 1px var(--tag-outline);
  }

  .contact { position: absolute; right: 24px; top: 592px; text-align: right; font-family: "Didact Gothic", sans-serif; color: var(--tag-white); }
  .contact__name { font-size: 22px; letter-spacing: 1.5px; line-height: 28px; }
  .contact__carrier { font-size: 18px; line-height: 24px; margin-bottom: 12px; }
  .contact__line { font-size: 18px; line-height: 28px; padding-right: 6px; }
  .contact__hours { position: absolute; right: 30px; top: 776px; font-family: "Didact Gothic", sans-serif; font-size: 28px; line-height: 1.2; color: var(--tag-white); white-space: nowrap; }
</style>
</head>
<body>
<main class="canvas">

  <section class="page page--front">
    <div class="marble" role="img" aria-label="Bunter Marmorhintergrund in Rot, Orange, Gelb und Blau"></div>
    <div class="silhouette silhouette--front" role="img" aria-label="Schwarze Silhouette eines Sprayers mit Kappe und Spraydose"></div>

    <div class="brand-mark"><div class="brand-name">Initiative für bunte Freizeitkultur</div></div>
    <div class="treff-name">Jugendtreff Korvane</div>
    <div class="treff-carrier">Initiative für bunte Freizeitkultur e.V.</div>

    <span class="tag" style="left:128px; top:238px; font-size:26px;">Tischtennis</span>

    <span class="tag tag--up" style="left:50px; top:368px;">Billard</span>
    <span class="tag tag--up" style="left:85px; top:368px;">Fitness</span>
    <span class="tag" style="left:128px; top:270px;">Räume</span>
    <span class="tag" style="left:128px; top:304px;">selbst</span>
    <span class="tag" style="left:128px; top:338px;">gestalten</span>

    <span class="tag tag--title" style="left:51px; top:378px;">Jugendtreff</span>
    <span class="tag tag--title" style="left:55px; top:421px;">Korvane</span>

    <span class="tag" style="left:76px; top:474px;">essen &amp;</span>
    <span class="tag" style="left:42px; top:508px;">Getränke</span>
    <span class="tag" style="left:130px; top:552px;">GX7</span>

    <span class="tag tag--down" style="left:236px; top:551px;">chillen</span>
    <span class="tag tag--down" style="left:276px; top:481px;">Werkstatt</span>
    <span class="tag tag--down" style="left:317px; top:428px;">Free WLAN</span>
  </section>

  <section class="page page--back">
    <div class="marble" role="img" aria-label="Bunter Marmorhintergrund mit Wirbeln in Blau, Rot und Orange"></div>
    <div class="silhouette silhouette--back" role="img" aria-label="Schwarze Silhouette eines Sprayers, kopfüber"></div>

    <div class="handle-block">
      <div class="handle-text">
        <div class="handle-name">jugendtreff_korvane</div>
        <div class="handle-follow">Follow us on Fotello</div>
      </div>
      <div class="handle-icon"></div>
    </div>

    <div class="contact">
      <div class="contact__name">Jugendtreff Korvane</div>
      <div class="contact__carrier">Initiative für bunte Freizeitkultur e.V.</div>
      <div class="contact__line">Lindenhofer Straße 12</div>
      <div class="contact__line">08123 Feldau</div>
      <div class="contact__line">01234/ 567 8901</div>
      <div class="contact__line">kontakt@treff-korvane.de</div>
    </div>
    <div class="contact__hours">Öffnungszeiten: Di - Fr 14:00Uhr bis 18:30Uhr</div>
  </section>

</main>
</body>
</html>
```